Design a web site for my business - Brellan Coatworks Mackaby.

We are a family business that handles design, fabrication and installation of powder coated aluminum, stainless steel and glass products. Including handrails, privacy slat screens, electric gates and pool fencing. We are based in the Whitsundays in North Queensland and service an area from Airlie Beach to Townsville.

Target Market(s)

Domestic and commercial

Industry/Entity Type

fabrication - manufacturing

Coding

Coded - Design and coding required

Number of Pages Required

5+ page

Colors
0054AA
0677BA
7BADD7
CADEEF
E8F1F8

Requirements
Must have
• photo galleries, contact page, one page for privacy screens, balustrades, glass fencing, stainless steel handrail, powder coated aluminium handrails and pool fencing

```html
<!DOCTYPE html>
<html lang="en">
<head>
<meta charset="utf-8">
<title>Products — Brellan Coatworks Mackaby</title>
<link href="https://fonts.googleapis.com/css2?family=Montserrat:wght@600;700&family=Inter:wght@400;500;600&display=swap" rel="stylesheet">
<style>
:root{
  --ink:#1c2124;
  --text:#3d4449;
  --muted:#6b7278;
  --page:#f4f8fb;
  --card:#ffffff;
  --line:#e2e7eb;
  --blue:#0054AA;
  --blue-mid:#0677BA;
  --blue-soft:#7BADD7;
  --dark:#1f2427;
  --footer:#1b2124;
}
*{box-sizing:border-box;margin:0;padding:0}
html,body{width:1200px;height:2706px;overflow:hidden}
body{background:var(--page);font-family:"Inter",Arial,sans-serif;color:var(--text);position:relative}
.header{height:77px;background:#f7fafc;border-bottom:1px solid var(--line);display:flex;align-items:center;padding:0 62px}
.brand{font-family:"Montserrat",Arial,sans-serif;font-weight:600;font-size:21px;color:var(--ink);letter-spacing:-.3px;text-transform:uppercase}
.nav{display:flex;gap:31px;margin-left:145px}
.nav a{font-size:14px;font-weight:500;color:#3a4146;text-decoration:none;letter-spacing:.3px}
.nav a.active{color:var(--blue);font-weight:600;border-bottom:2px solid var(--blue);padding-bottom:6px;margin-top:-4px}
.cta{margin-left:auto;background:var(--ink);color:#fff;font-size:13px;font-weight:600;letter-spacing:.8px;padding:11px 21px;border-radius:5px}
.hero{padding:43px 62px 0}
.hero h1{font-family:"Montserrat",Arial,sans-serif;font-weight:700;font-size:64px;line-height:68px;color:var(--ink);letter-spacing:-.8px}
.hero p{margin-top:28px;font-size:17px;line-height:27px;max-width:740px;color:#444b50}
.grid{position:absolute;left:62px;top:390px;width:1076px;display:grid;grid-template-columns:526px 526px;gap:24px}
.card{background:var(--card);border:1px solid var(--line);border-radius:10px;overflow:hidden;position:relative}
.photo{height:373px}
.badge{position:absolute;left:15px;top:17px;background:var(--ink);color:#fff;font-size:11.5px;font-weight:500;padding:4px 15px;border-radius:20px;letter-spacing:.2px}
.badge.blue{background:var(--blue)}
.body{padding:30px 30px 30px}
.body h2{font-family:"Montserrat",Arial,sans-serif;font-weight:600;font-size:31px;color:var(--ink);letter-spacing:-.2px}
.body p{margin-top:17px;font-size:15.3px;line-height:24.2px;color:#4a5156}
.tags{display:flex;gap:11px;margin-top:20px}
.tag{border:1px solid var(--line);font-size:11.5px;padding:4px 12px;color:#30373b;border-radius:2px}
.btn{margin-top:31px;height:48px;border:1.5px solid var(--ink);display:flex;align-items:center;justify-content:center;font-size:13.5px;font-weight:600;letter-spacing:1px;color:var(--ink)}
.excellence{position:absolute;left:62px;top:1915px;width:1076px;height:310px;border-radius:12px;overflow:hidden;background:linear-gradient(165deg,#262b2e 0%,#23282b 50%,#1d2225 50.2%,#1c2023 100%);padding:74px 0 0 60px;color:#fff}
.excellence h2{font-family:"Montserrat",Arial,sans-serif;font-weight:700;font-size:46px;line-height:54px}
.excellence p{margin-top:16px;font-size:17px;line-height:27px;color:#d5d9dc;max-width:540px}
.stats{position:absolute;right:60px;top:100px;display:flex;gap:15px}
.stat{width:150px;height:127px;border:1px solid #4a5155;background:#3a4044;border-radius:8px;display:flex;flex-direction:column;align-items:center;padding-top:22px;text-align:center;font-size:15.5px;line-height:22.5px;color:#eef1f3}
.stat svg{margin-bottom:8px}
.footer{position:absolute;left:0;top:2300px;width:1200px;height:406px;background:var(--footer);color:#8d959a}
.f-about{position:absolute;left:62px;top:117px;width:245px}
.f-brand{font-family:"Inter",Arial,sans-serif;font-size:14px;color:#2a3135;margin-bottom:32px;letter-spacing:.5px}
.f-about p{font-size:15px;line-height:24px;color:#8a9297}
.f-col{position:absolute;top:80px}
.f-col h3{font-family:"Inter",Arial,sans-serif;font-weight:500;font-size:15px;letter-spacing:2px;color:#d8dcdf;margin-bottom:20px}
.f-col li{list-style:none;font-size:11.5px;line-height:28px;color:#858d92}
.f-bottom{position:absolute;left:62px;right:0;top:332px;border-top:1px solid #2b3236;padding-top:36px;font-size:11px;color:#72797e}
</style>
</head>
<body>
<header class="header">
  <div class="brand">Brellan Coatworks Mackaby</div>
  <nav class="nav"><a href="#">Home</a><a class="active" href="#">Products</a><a href="#">Process</a><a href="#">Projects</a></nav>
  <div class="cta">REQUEST A QUOTE</div>
</header>

<section class="hero">
  <h1>Architectural Metal &amp;<br>Glass Solutions</h1>
  <p>Precision-engineered fabrications designed for the Whitsundays' unique coastal environment. From marine-grade stainless steel to powder-coated architectural aluminum.</p>
</section>

<main class="grid">
  <article class="card">
    <div class="photo" role="img" aria-label="Glass balustrade with stainless handrail on a deck overlooking turquoise bay and islands" style="background:linear-gradient(135deg,#7fc3d8 0%,#3aa4c0 35%,#9aa39a 60%,#cfc8bd 100%)"></div>
    <span class="badge">STAINLESS STEEL &amp; GLASS</span>
    <div class="body">
      <h2>Glass &amp; Stainless Handrails</h2>
      <p>Engineered for unobstructed views and maximum durability. We utilize 316 Marine Grade Stainless Steel and toughened architectural glass, ensuring your balustrade withstands the salt-heavy Whitsunday breeze while maintaining a mirror-finish brilliance.</p>
      <div class="tags"><span class="tag">316 Marine Grade</span><span class="tag">12mm Toughened Glass</span><span class="tag">Satin or Mirror Finish</span></div>
      <div class="btn">EXPLORE DESIGNS</div>
    </div>
  </article>
  <article class="card">
    <div class="photo" role="img" aria-label="Dark aluminium slat privacy screens around a modern outdoor lounge area" style="background:linear-gradient(120deg,#4a4e51 0%,#7d7c77 45%,#b9b3a8 70%,#6f7a5c 100%)"></div>
    <span class="badge">ALUMINUM SLATTING</span>
    <div class="body">
      <h2>Privacy Slat Screens</h2>
      <p>Maintain your sanctuary with our customizable aluminum slat systems. Available in a vast range of powder-coated colors, these screens offer the perfect balance of ventilation, light, and total privacy for high-end residential properties.</p>
      <div class="tags"><span class="tag">Powder-Coated Aluminum</span><span class="tag">Custom Spacing</span><span class="tag">UV Resistant</span></div>
      <div class="btn">VIEW COLOR RANGE</div>
    </div>
  </article>
  <article class="card">
    <div class="photo" role="img" aria-label="Black slatted electric sliding gate with stone pillar in front of a tropical home" style="background:linear-gradient(180deg,#8fc2e0 0%,#4f7a45 35%,#2c2f30 62%,#c9c9c6 85%)"></div>
    <span class="badge blue">AUTOMATION</span>
    <div class="body">
      <h2>Custom Electric Gates</h2>
      <p>Secure your property with an architectural statement. Our electric gates feature Italian-made automation systems integrated into heavy-duty frames. Designed for reliability, ease of use, and seamless aesthetic integration with your home’s perimeter.</p>
      <div class="tags"><span class="tag">Smart Integration</span><span class="tag">Swing or Sliding</span><span class="tag">Intercom Ready</span></div>
      <div class="btn">AUTOMATION OPTIONS</div>
    </div>
  </article>
  <article class="card">
    <div class="photo" role="img" aria-label="Frameless glass pool fence beside an infinity pool and timber deck overlooking islands" style="background:linear-gradient(170deg,#7ec0e6 0%,#3e8a6a 30%,#38b5dc 55%,#9a5c3b 85%)"></div>
    <span class="badge">FRAMELESS GLASS</span>
    <div class="body">
      <h2>Luxury Pool Fencing</h2>
      <p>Compliance meets elegance. Our frameless glass pool fencing provides a safe barrier without interrupting the visual flow of your poolside oasis. Using heavy-duty spigots and self-closing hydraulic hinges for the ultimate in safety and style.</p>
      <div class="tags"><span class="tag">AS1926.1 Compliant</span><span class="tag">Hydraulic Hinges</span><span class="tag">Non-Slip Hardware</span></div>
      <div class="btn">GET A QUOTE</div>
    </div>
  </article>
</main>

<section class="excellence">
  <h2>Engineered for<br>Excellence</h2>
  <p>All our products are fabricated in-house at our Airlie Beach facility using premium raw materials sourced from Australian suppliers.</p>
  <div class="stats">
    <div class="stat">
      <svg width="26" height="28" viewBox="0 0 24 26" fill="none" stroke="#7BADD7" stroke-width="2"><path d="M12 2l9 3.5v7c0 5.5-4 9.5-9 11.5C7 22 3 18 3 12.5v-7z"/></svg>
      Lifetime<br>Structural
    </div>
    <div class="stat">
      <svg width="26" height="28" viewBox="0 0 24 26" fill="none" stroke="#7BADD7" stroke-width="2"><path d="M12 24s8-7.5 8-14a8 8 0 0 0-16 0c0 6.5 8 14 8 14z"/><circle cx="12" cy="10" r="3"/></svg>
      Airlie Beach<br>Based
    </div>
  </div>
</section>

<footer class="footer">
  <div class="f-about">
    <div class="f-brand">BRELLAN COATWORKS</div>
    <p>Custom metal &amp; glass fabrication experts serving Airlie Beach, Cannonvale, and the surrounding islands.</p>
  </div>
  <div class="f-col" style="left:337px"><h3>PRODUCTS</h3><ul><li>Handrails</li><li>Slat Screens</li><li>Electric Gates</li><li>Pool Fencing</li></ul></div>
  <div class="f-col" style="left:612px"><h3>SERVICE AREAS</h3><ul><li>Airlie Beach</li><li>Townsville</li><li>Bowen</li><li>Mackay</li></ul></div>
  <div class="f-col" style="left:887px"><h3>LEGAL</h3><ul><li>Privacy Policy</li><li>Terms of Service</li></ul></div>
  <div class="f-bottom">© 2024 Brellan Coatworks Mackaby. All Rights Reserved. Australian Made.</div>
</footer>
</body>
</html>
```